Redesign of a facility management homepage

We need a redesign/an improved design of the facility management homepage (http://www.krt-lanzfeld.de/).
This websites offers detailed information on the "About us" as company, the "Services" provided and special information on facility and strata management. We would like to keep the structure of the website.
We need ideas/designs how this website could look more modern and confidential and appealing/pleasant for visitors at the same time and not losing the main purpose of information distribution.
The green color must be used since this is the basic color from our logo.
The blue in the background of the logo ist optional. So feel to use it or not.
We need no coding only design (.psd or as .ai)

```html
<!DOCTYPE html>
<html lang="de">
<head>
<meta charset="utf-8">
<title>KRT Lanzfeld – Facility Management</title>
<link rel="stylesheet" href="https://fonts.googleapis.com/css2?family=Roboto+Condensed:wght@400;700&family=Arimo:wght@400;700&display=swap">
<style>
:root{
  --bg:#2e2e2e;
  --panel:#f3f3f3;
  --card:#ffffff;
  --green:#2f8a34;
  --text:#555555;
  --heading:#111111;
  --btn:#ececec;
  --btn-arrow:#dcdcdc;
  --divider:#cfcfcf;
}
*{margin:0;padding:0;box-sizing:border-box}
html,body{width:1200px;height:1200px;overflow:hidden}
body{background:var(--bg);font-family:"Arimo",Arial,sans-serif;color:var(--text);position:relative}
.social{position:absolute;top:10px;right:16px;display:flex;gap:4px}
.social span{width:27px;height:27px;background:var(--green);display:block}
.brand{position:absolute;left:38px;top:40px;display:flex;align-items:center;gap:12px}
.brand-mark{width:26px;height:26px;background:var(--green)}
.brand-name{font-family:"Roboto Condensed",Arial,sans-serif;font-weight:700;font-size:60px;color:#fff;letter-spacing:2px;line-height:1}
.tagline{position:absolute;left:273px;top:102px;color:#e6e6e6;font-size:15px;line-height:19px}
.date{position:absolute;right:19px;top:124px;color:#e6e6e6;font-size:12px}
.panel{position:absolute;left:21px;top:150px;width:1160px;height:1100px;background:var(--panel);border-radius:4px}
.nav{position:absolute;left:103px;top:35px;display:flex}
.nav a{width:162px;height:55px;display:flex;align-items:center;justify-content:center;font-size:12px;color:#444;text-decoration:none;letter-spacing:.3px;border-left:1px solid var(--divider)}
.nav a.active{background:var(--green);color:#fff;border-radius:4px;margin-right:14px;width:136px;border-left:none}
.hero{position:absolute;left:35px;top:116px;width:1083px;height:312px;border-radius:4px;overflow:hidden;
  background:linear-gradient(180deg,#4aa3e8 0%,#c9c2ae 40%,#b8ab92 62%,#ddd8cc 100%)}
.hero-label{position:absolute;left:0;top:234px;width:310px;height:64px;background:var(--green);border-radius:0 4px 4px 0;
  color:#fff;font-family:"Roboto Condensed",Arial,sans-serif;font-weight:700;font-size:23px;line-height:26px;padding:6px 0 0 147px}
.dots{position:absolute;right:66px;top:294px;display:flex;gap:5px}
.dots span{width:10px;height:10px;border-radius:50%;background:#333}
.dots span.on{background:#1e88c8}
.cards{position:absolute;left:35px;top:450px;display:grid;grid-template-columns:repeat(4,253px);grid-template-rows:253px 253px;column-gap:23.5px;row-gap:11px}
.card{background:var(--card);border-radius:4px;position:relative;padding:74px 19px 0 19px}
.card-head{position:absolute;left:10px;top:14px;display:flex;align-items:center;gap:10px}
.badge{width:41px;height:41px;flex:none;border-radius:50%;background:var(--green);color:#fff;font-family:"Roboto Condensed",Arial,sans-serif;font-weight:700;font-size:22px;display:flex;align-items:center;justify-content:center}
.card h2{font-family:"Roboto Condensed",Arial,sans-serif;font-weight:700;font-size:15px;color:var(--heading);white-space:nowrap}
.card p{font-size:11px;line-height:15px;text-align:justify}
.card p+p{margin-top:15px}
.more{position:absolute;left:19px;top:206px;width:103px;height:26px;background:var(--btn);border-radius:4px;display:flex;font-size:10px;color:#333;overflow:hidden}
.more b{flex:1;font-weight:400;padding-left:8px;line-height:26px}
.more i{width:24px;background:var(--btn-arrow);font-style:normal;text-align:center;line-height:26px}
.info{position:absolute;top:984px;width:530px;height:120px;background:var(--card);border-radius:4px;padding:12px 11px}
.info-left{left:35px}
.info-right{left:588px}
.info h3{font-family:"Roboto Condensed",Arial,sans-serif;font-weight:700;font-size:16px;color:var(--heading);margin-bottom:8px}
.info p{font-size:12px;line-height:15px;text-align:justify}
</style>
</head>
<body>
<div class="social"><span></span><span></span><span></span><span></span></div>
<div class="brand"><span class="brand-mark"></span><span class="brand-name">KRT</span></div>
<div class="tagline">Kraft Raum Technik GmbH Lanzfeld<br>Ihr Partner vor Ort.</div>
<div class="date">Friday, 13 June 2014</div>

<main class="panel">
  <nav class="nav">
    <a class="active" href="#">HOME</a>
    <a href="#">ABOUT US</a>
    <a href="#">WHAT WE DO</a>
    <a href="#">WHAT WE OFFER</a>
    <a href="#">PRICING</a>
    <a href="#">CONTACT</a>
  </nav>

  <section class="hero" role="img" aria-label="Photo of a building under renovation with scaffolding along its facade">
    <div class="hero-label">Haustechnik<br>Überwachung</div>
    <div class="dots"><span class="on"></span><span></span><span></span><span></span><span></span></div>
  </section>

  <section class="cards">
    <article class="card"><div class="card-head"><span class="badge">A</span><h2>Haustechnik Überwachung</h2></div>
      <p>Lorem ipsum dolor sit amet, consectetur adipiscing elit. Aenean turpis nibh, lacinia vel massa in, pharetra tincidunt libero. Nullam eu urna varius nulla viverra ornare. Pellentesque quis pharetra dui, a consequat risus. Donec ligula mi, bibendum in malesuada nec, adipiscing eget purus.</p>
      <a class="more"><b>Read More</b><i>&gt;</i></a></article>
    <article class="card"><div class="card-head"><span class="badge">B</span><h2>Hausmeisterdienst</h2></div>
      <p>consectetur adipiscing elit. Duis vel molestie mi, sit amet convallis turpis. Quisque egestas volutpat ligula, et cursus erat imperdiet non. Vivamus mollis enim non tincidunt malesuada. Sed nisi eros, mattis vestibulum sem quis, ullamcorper condimentum justo. Pellentesque dictum vulputate sem quis</p>
      <a class="more"><b>Read More</b><i>&gt;</i></a></article>
    <article class="card"><div class="card-head"><span class="badge">C</span><h2>Reinigung Kehrdienst</h2></div>
      <p>feugiat. In tristique tellus id mauris lacinia, vel eleifend lorem sollicitudin.</p>
      <p>Maecenas volutpat mauris vel metus gravida aliquet. Cum sociis natoque penatibus et magnis dis parturient montes, nascetur ridiculus mus. Interdum et malesuada fames ac ante</p>
      <a class="more"><b>Read More</b><i>&gt;</i></a></article>
    <article class="card"><div class="card-head"><span class="badge">D</span><h2>Winterdienst</h2></div>
      <p>primis in faucibus. Mauris vitae lorem eget nulla pretium luctus quis nec urna. Fusce pharetra iaculis mauris, sed consectetur arcu consectetur quis. Aenean cursus consequat vulputate. Maecenas turpis mi, mattis vitae augue ut, fringilla tempor risus.</p>
      <a class="more"><b>Read More</b><i>&gt;</i></a></article>
    <article class="card"><div class="card-head"><span class="badge">E</span><h2>Garten – Außenanlagen</h2></div>
      <p>Lorem ipsum dolor sit amet, consectetur adipiscing elit. Aenean turpis nibh, lacinia vel massa in, pharetra tincidunt libero. Nullam eu urna varius nulla viverra ornare. Pellentesque quis pharetra dui, a consequat risus. Donec ligula mi, bibendum in malesuada nec, adipiscing eget purus.</p>
      <a class="more"><b>Read More</b><i>&gt;</i></a></article>
    <article class="card"><div class="card-head"><span class="badge">F</span><h2>Instandhaltungsmanagement</h2></div>
      <p>consectetur adipiscing elit. Duis vel molestie mi, sit amet convallis turpis. Quisque egestas volutpat ligula, et cursus erat imperdiet non. Vivamus mollis enim non tincidunt malesuada. Sed nisi eros, mattis vestibulum sem quis, ullamcorper condimentum justo. Pellentesque dictum vulputate sem quis</p>
      <a class="more"><b>Read More</b><i>&gt;</i></a></article>
    <article class="card"><div class="card-head"><span class="badge">G</span><h2>Der Erfolg für Ihre Immobile</h2></div>
      <p>feugiat. In tristique tellus id mauris lacinia, vel eleifend lorem sollicitudin.</p>
      <p>Maecenas volutpat mauris vel metus gravida aliquet. Cum sociis natoque penatibus et magnis dis parturient montes, nascetur ridiculus mus. Interdum et malesuada fames ac ante</p>
      <a class="more"><b>Read More</b><i>&gt;</i></a></article>
    <article class="card"><div class="card-head"><span class="badge">H</span><h2>Facility Management</h2></div>
      <p>primis in faucibus. Mauris vitae lorem eget nulla pretium luctus quis nec urna. Fusce pharetra iaculis mauris, sed consectetur arcu consectetur quis. Aenean cursus consequat vulputate. Maecenas turpis mi, mattis vitae augue ut, fringilla tempor risus.</p>
      <a class="more"><b>Read More</b><i>&gt;</i></a></article>
  </section>

  <section class="info info-left">
    <h3>Gebäudeverwaltung</h3>
    <p>primis in faucibus. Mauris vitae lorem eget nulla pretium luctus quis nec urna. Fusce pharetra iaculis mauris, sed consectetur arcu consectetur quis. Aenean cursus consequat vulputate.</p>
  </section>
  <section class="info info-right">
    <h3>Vermietung</h3>
    <p>primis in faucibus. Mauris vitae lorem eget nulla pretium luctus quis nec urna. Fusce pharetra iaculis mauris, sed consectetur arcu consectetur quis. Aenean cursus consequat vulputate.</p>
  </section>
</main>
</body>
</html>
```